Envelope design

We need a envelope design for a professional services firm called Brindlemoor Tax Consultancy Inc. The firm is essentially a very specialized tax accounting firm - instead of serving the end consumer, we support other public accounting firms in the area of Canadian and U.S. tax advisory and compliance (i.e. they call us on tax issues too complex for the general practitioner). Our byline is "Tax Support Services for Public Accounting Firms". Our postcard should utilize our logo and be based on colours present in our logo (see file attached). The final design needs to convey professionalism and trustworthiness (we're hired by accountants after all!) while being creative and eye-catching. Eye-catching is critical, since many prospective recipients will not have heard from me before and I want them to read the postcard.
At lot of design work has already been done here. I've attached a number of sample files showing logo and letterhead designs. Please note that the letterhead hasn't yet been updated for the new logo. This is happening in a separate design competition.
Updates
Project Deadline Extended Reason: Deadline is extended because I am pricing the extra cost of having colour right to the edge of the envelopes. This will help me design on final design. Pricing should come in on Monday. Added Saturday, February 20, 2016

```html
<!DOCTYPE html>
<html lang="en">
<head>
<meta charset="utf-8">
<title>Brindlemoor Tax Consultancy – Envelope Dieline</title>
<link rel="stylesheet" href="https://fonts.googleapis.com/css2?family=Montserrat:wght@500&family=Arimo&display=swap">
<style>
  :root {
    --paper: #ffffff;
    --brand-blue: #1f94d2;
    --trim-red: #d2232a;
    --safe-cyan: #00aee8;
    --fold-green: #1aa94a;
    --glue-grey: #d3d4d6;
    --ink: #231f20;
    --ink-soft: #58595b;
    --label-blue: #1f7fc4;
  }
  html, body {
    margin: 0;
    padding: 0;
    width: 1200px;
    height: 1200px;
    overflow: hidden;
    background: var(--paper);
  }
  .dieline { display: block; width: 1200px; height: 1200px; }
  .bleed-band { fill: var(--brand-blue); }
  .panel-white { fill: var(--paper); }
  .glue-strip { fill: var(--glue-grey); }
  .trim-line { fill: none; stroke: var(--trim-red); stroke-width: 4; stroke-linejoin: round; }
  .safe-line { fill: none; stroke: var(--safe-cyan); stroke-width: 4; stroke-linejoin: round; }
  .fold-line { fill: none; stroke: var(--fold-green); stroke-width: 4; stroke-dasharray: 6 6; }
  .legend-box { fill: var(--paper); stroke: var(--ink); stroke-width: 2; }
  .legend-text { font-family: "Arimo", Arial, sans-serif; font-size: 26px; fill: var(--ink); }
  .firm-name { font-family: "Montserrat", Arial, sans-serif; font-weight: 500; font-size: 16px; letter-spacing: 0.6px; fill: var(--ink); }
  .firm-tagline { font-family: "Montserrat", Arial, sans-serif; font-weight: 500; font-size: 9px; letter-spacing: 1.6px; fill: var(--ink-soft); }
  .firm-mark { fill: var(--brand-blue); }
  .return-address { font-family: "Montserrat", Arial, sans-serif; font-weight: 500; font-size: 17px; letter-spacing: 4.4px; fill: var(--ink); }
  .contact-label { font-family: "Arimo", Arial, sans-serif; font-size: 13px; fill: var(--label-blue); }
  .contact-value { font-family: "Arimo", Arial, sans-serif; font-size: 13px; fill: var(--ink); }
  .contact-arrow { fill: none; stroke: var(--ink); stroke-width: 1.6; }
</style>
</head>
<body>
<svg class="dieline" viewBox="0 0 1500 1500" xmlns="http://www.w3.org/2000/svg">
  <rect class="bleed-band" x="0" y="892" width="1500" height="608"/>
  <rect class="panel-white" x="103" y="892" width="1294" height="84"/>

  <rect class="glue-strip" x="24" y="437" width="51" height="418"/>
  <rect class="glue-strip" x="1425" y="437" width="51" height="420"/>
  <rect class="glue-strip" x="123" y="1287" width="1254" height="78"/>

  <path class="trim-line" d="M97 325 L105 160 Q107 132 135 132 L1365 132 Q1393 132 1395 160 L1403 325
        L1480 412 L1480 857 L1403 890
        L1388 1335 Q1387 1368 1355 1368 L145 1368 Q113 1368 112 1335 L97 890
        L20 855 L20 412 Z"/>

  <path class="safe-line" d="M108 312 L116 170 Q118 145 145 145 L1355 145 Q1382 145 1384 170 L1393 312 Z"/>
  <rect class="safe-line" x="108" y="335" width="1285" height="547"/>
  <path class="safe-line" d="M108 902 L1393 902 L1383 1245 L118 1245 Z"/>

  <rect class="fold-line" x="97" y="323" width="1306" height="567"/>

  <rect class="legend-box" x="836" y="573" width="334" height="37"/>
  <text class="legend-text" x="1157" y="601" text-anchor="end">TRIM / DIE CUT</text>
  <line class="trim-line" x1="1197" y1="590" x2="1312" y2="590"/>
  <rect class="legend-box" x="836" y="625" width="334" height="37"/>
  <text class="legend-text" x="1157" y="653" text-anchor="end">SAFE MARGIN</text>
  <line class="safe-line" x1="1197" y1="646" x2="1312" y2="646"/>
  <rect class="legend-box" x="837" y="677" width="334" height="37"/>
  <text class="legend-text" x="1158" y="705" text-anchor="end">FOLD</text>
  <line class="fold-line" x1="1202" y1="693" x2="1312" y2="693"/>

  <rect class="firm-mark" x="262" y="660" width="97" height="96"/>
  <text class="firm-name" x="148" y="783">BRINDLEMOOR TAX CONSULTANCY</text>
  <text class="firm-tagline" x="148" y="800">TAX SUPPORT FOR PUBLIC ACCOUNTING FIRMS</text>
  <text class="return-address" x="147" y="840">18-410 Calloway Street, Dartmouth, Nova Scotia, Canada B3B 2K7</text>

  <g class="contact-row" transform="rotate(180 750 935)">
    <path class="contact-arrow" d="M307 931 L312 935 L307 939 M312 931 L317 935 L312 939"/>
    <text class="contact-label" x="325" y="940">PHONE</text>
    <text class="contact-value" x="388" y="940">902.555.0147 | 902.555.0193</text>
    <path class="contact-arrow" d="M630 931 L635 935 L630 939 M635 931 L640 935 L635 939"/>
    <text class="contact-label" x="650" y="940">EMAIL</text>
    <text class="contact-value" x="702" y="940">MORGAN@BRINDLEMOORTAX.CA</text>
    <path class="contact-arrow" d="M982 931 L987 935 L982 939 M987 931 L992 935 L987 939"/>
    <text class="contact-label" x="1003" y="940">WEB</text>
    <text class="contact-value" x="1045" y="940">BRINDLEMOORTAX.CA</text>
  </g>
</svg>
</body>
</html>
```